Hispanic Financial Counseling and Advocate Firm seeks business card design

Looking for a clean, professional business card design. This is a firm that specializes in providing financial education, coaching, and planning to the Hispanic community. The name of the company is Valemar, which means to prosper. We need a design that is clean, professional, and invokes trust, professionalism, but also welcoming. Our logo is a plant growing from a hand to give the messaging of of being in control of growing your financial future and security. Its part of a larger organization names Celesta Financial Group, who's logo is a tree with multi colored branches. We have the back of the card designed so we just need the front designed. the back is blue, so front needs to be a different background color, not blue.

Target Market(s)

Hispanic Community looking to better their future

Industry/Entity Type

financial services

Contact Information for Business Card

contact info: Anselmo Ibarra Jr, 951-555-0147, info@celestafinancialgroup.example. Celestafinancialgroup.example. tag line: Para un futuro mas seguro!

Requirements
Must have
• basics: logo, contact info.
Nice to have
• possibly incorporate the tree logo provided somehow
Should not have
• should not look like the back, needs to be different from the back provided.

```html
<!DOCTYPE html>
<html lang="es">
<head>
<meta charset="utf-8">
<title>Valemar – Tarjeta de presentación</title>
<link rel="stylesheet" href="https://fonts.googleapis.com/css2?family=Montserrat:wght@500;700;800&family=Barlow+Condensed:wght@400;600&family=Roboto:wght@400&display=swap">
<style>
  :root {
    --backdrop: #cbcbcb;
    --paper: #ffffff;
    --navy: #002440;
    --brand-green: #5ce000;
    --brand-tint: #e3f8d2;
    --ink-blue: #3b5a8f;
    --white: #ffffff;
    --leaf-green: #7be11a;
    --leaf-cyan: #36c6f4;
    --leaf-pink: #f2395e;
    --leaf-violet: #9b6cf0;
    --leaf-gold: #f5b21b;
  }
  * { margin: 0; padding: 0; box-sizing: border-box; }
  html, body {
    width: 1200px; height: 846px; overflow: hidden;
    background: var(--backdrop);
  }
  .card {
    position: absolute; left: 346px; width: 509px; height: 290px;
  }
  .card--front { top: 113px; background: var(--paper); }
  .card--back { top: 443px; background: var(--navy); }

  /* Front */
  .brand-dot {
    position: absolute; left: 82px; top: 46px; width: 96px; height: 96px;
    border-radius: 50%; background: var(--brand-tint);
  }
  .brand-name {
    position: absolute; left: 37px; top: 151px;
    font: 700 46px/1 "Montserrat", sans-serif;
    color: var(--brand-green); letter-spacing: -0.5px;
  }
  .brand-descriptor {
    position: absolute; left: 38px; top: 200px;
    font: 700 11px/1 "Montserrat", sans-serif;
    color: var(--ink-blue); letter-spacing: 1.3px;
  }
  .tagline {
    position: absolute; left: 38px; top: 228px;
    font: 600 17px/1 "Barlow Condensed", sans-serif;
    color: var(--ink-blue);
  }
  .divider {
    position: absolute; width: 1px;
  }
  .card--front .divider { left: 248px; top: 163px; height: 80px; background: var(--ink-blue); }
  .contact { position: absolute; left: 275px; top: 160px; }
  .contact__name {
    font: 800 14.5px/1 "Montserrat", sans-serif;
    color: var(--brand-green); margin-bottom: 10px; letter-spacing: 0.2px;
  }
  .contact__row {
    display: flex; align-items: center; height: 20px;
    font: 400 15px/1 "Barlow Condensed", sans-serif; color: var(--ink-blue);
  }
  .contact__row svg { width: 18px; height: 18px; margin-right: 9px; flex: none; }

  /* Back */
  .card--back .divider { left: 197px; top: 20px; height: 159px; background: var(--white); }
  .mark-dot {
    position: absolute; left: 70px; top: 46px; width: 104px; height: 104px;
    border-radius: 50%; background: #0c3a5e;
  }
  .group-name {
    position: absolute; left: 219px; top: 62px;
    font-family: "Montserrat", sans-serif; font-weight: 500; color: var(--white);
  }
  .group-name__main { display: block; font-size: 52px; line-height: 1; letter-spacing: -1px; }
  .group-name__sub { display: block; font-size: 20px; line-height: 1; margin-top: 10px; letter-spacing: 0.5px; }
  .services {
    position: absolute; left: 0; right: 0; top: 218px;
    text-align: center; list-style: none;
    font: 400 15px/19px "Roboto", sans-serif; color: var(--white);
  }
  .leaf {
    display: inline-block; width: 6px; height: 11px; margin: 0 3px 0 5px;
    border-radius: 50% 50% 50% 50% / 70% 70% 30% 30%;
    vertical-align: -1px;
  }
  .leaf--green { background: var(--leaf-green); }
  .leaf--cyan { background: var(--leaf-cyan); }
  .leaf--pink { background: var(--leaf-pink); }
  .leaf--violet { background: var(--leaf-violet); }
  .leaf--gold { background: var(--leaf-gold); }
</style>
</head>
<body>

<section class="card card--front" aria-label="Frente de la tarjeta">
  <div class="brand-dot"></div>
  <div class="brand-name">Valemar</div>
  <p class="brand-descriptor">SERVICIOS FINANCIEROS</p>
  <p class="tagline">PARA UN FUTURO MAS SEGURO!</p>
  <div class="divider"></div>
  <div class="contact">
    <p class="contact__name">Anselmo Ibarra Jr</p>
    <p class="contact__row">
      <svg viewBox="0 0 24 24" fill="none" stroke="#5ce000" stroke-width="2" stroke-linecap="round" stroke-linejoin="round"><path d="M22 16.9v3a2 2 0 0 1-2.2 2 19.8 19.8 0 0 1-8.6-3.1 19.5 19.5 0 0 1-6-6A19.8 19.8 0 0 1 2.1 4.2 2 2 0 0 1 4.1 2h3a2 2 0 0 1 2 1.7c.1 1 .4 1.9.7 2.8a2 2 0 0 1-.5 2.1L8 9.9a16 16 0 0 0 6 6l1.3-1.3a2 2 0 0 1 2.1-.4c.9.3 1.8.6 2.8.7a2 2 0 0 1 1.7 2z"/><path d="M15 2a7 7 0 0 1 7 7"/><path d="M15 6a3 3 0 0 1 3 3"/></svg>
      951-555-0147
    </p>
    <p class="contact__row">
      <svg viewBox="0 0 24 24" fill="#5ce000"><path d="M2 5h20v14H2z"/><path d="M2 5l10 8 10-8" fill="none" stroke="#fff" stroke-width="1.5"/><path d="M2 19l7.5-7M22 19l-7.5-7" stroke="#fff" stroke-width="1.5"/></svg>
      info@celestafinancialgroup.example
    </p>
    <p class="contact__row">
      <svg viewBox="0 0 24 24" fill="none" stroke="#5ce000" stroke-width="1.6"><circle cx="12" cy="12" r="10"/><ellipse cx="12" cy="12" rx="4.5" ry="10"/><path d="M2 12h20M4 7h16M4 17h16"/></svg>
      www.celestafinancialgroup.example
    </p>
  </div>
</section>

<section class="card card--back" aria-label="Reverso de la tarjeta">
  <div class="mark-dot"></div>
  <div class="divider"></div>
  <div class="group-name">
    <span class="group-name__main">Celesta</span>
    <span class="group-name__sub">Financial Group Inc</span>
  </div>
  <ul class="services">
    <li><span class="leaf leaf--green"></span>Inmigración <span class="leaf leaf--cyan"></span> Planificacion Financiera</li>
    <li><span class="leaf leaf--pink"></span>Seguros <span class="leaf leaf--violet"></span>Impuestos <span class="leaf leaf--pink"></span>Y mas</li>
    <li><span class="leaf leaf--gold"></span>Preparación de documentos</li>
  </ul>
</section>

</body>
</html>
```